Marketing flyer to advertise course vacancies

I am seeking something that is eye catching
A document that I can edit to list our courses and prices to try and gain further bookings on the courses.
I have attached our company logo, our website is www.brightpathskills.com.au for your viewing.
Our motto is Train today for a safer tomorrow, we would want this on the brochure.

```html
<!DOCTYPE html>
<html lang="en">
<head>
<meta charset="utf-8">
<title>BrightPath Skills – Courses and Prices</title>
<link rel="stylesheet" href="https://fonts.googleapis.com/css2?family=Montserrat:wght@500;600;700;800&family=Oswald:wght@500;600&display=swap">
<style>
:root{
  --red:#d7192f;
  --white:#ffffff;
  --ink:#1d1d1d;
  --rule:#9a9a9a;
  --sky-top:#6a9fd6;
  --sky-mid:#a7b8c9;
  --warm:#c8573f;
}
*{box-sizing:border-box;margin:0;padding:0}
html,body{width:1200px;height:1200px;overflow:hidden;background:var(--white)}
.flyer{position:relative;width:1200px;height:1200px;background:var(--white);font-family:"Montserrat",sans-serif}

/* left promo panel */
.promo{position:absolute;left:0;top:0;width:620px;height:1200px;background:var(--red)}
.brand-oval{position:absolute;left:13px;top:20px;width:594px;height:337px;background:var(--white);border-radius:50%;display:flex;align-items:center;justify-content:center;gap:14px}
.brand-dot{width:26px;height:26px;border-radius:50%;background:var(--red)}
.brand-name{font-family:"Montserrat",sans-serif;font-weight:800;font-size:44px;color:var(--red);letter-spacing:.5px}
.motto{position:absolute;left:30px;top:386px;width:580px;color:var(--white);font-weight:700;font-size:52px;line-height:66px;letter-spacing:0}
.motto-line{display:block;white-space:nowrap}
.photo{position:absolute;left:27px;top:531px;width:566px;height:455px;background:linear-gradient(180deg,var(--sky-top) 0%,var(--sky-mid) 55%,var(--warm) 82%,var(--red) 100%)}
.contact-note{position:absolute;left:27px;top:985px;width:570px;color:var(--white);font-weight:700;font-size:17px;line-height:23px}
.phone{position:absolute;left:27px;top:1042px;display:flex;align-items:center;gap:14px;color:var(--white)}
.phone-num{font-family:"Oswald",sans-serif;font-weight:600;font-size:90px;line-height:96px;letter-spacing:3px}
.email{position:absolute;left:27px;top:1136px;display:flex;align-items:center;gap:16px;color:var(--white);font-family:"Oswald",sans-serif;font-weight:600;font-size:32px;letter-spacing:1px}

/* right price list */
.list-title{position:absolute;left:633px;top:24px;width:547px;height:49px;background:var(--red);color:var(--white);font-weight:600;font-size:29px;line-height:49px;text-align:center;letter-spacing:.3px}
.price-table{position:absolute;left:633px;top:73px;width:547px;border-collapse:collapse;font-size:13.5px;color:var(--ink)}
.price-table th{height:24px;color:var(--red);font-weight:700;font-size:12.5px;text-transform:uppercase;text-align:left;padding-left:7px;border-bottom:1px solid var(--rule)}
.price-table td{height:25.6px;padding-left:7px;border:1px solid var(--rule);border-top:none;font-weight:500}
.price-table th.col-duration,.price-table th.col-cost,.price-table td.dur,.price-table td.cost{text-align:center;padding-left:0}
.price-table td:first-child{border-left:none}
.col-course{width:331px}.col-duration{width:109px}.col-cost{width:107px}
.web-bar{position:absolute;left:633px;top:1140px;width:567px;height:60px;background:var(--red);display:flex;align-items:center;justify-content:center;gap:18px;color:var(--white);font-family:"Oswald",sans-serif;font-weight:600;font-size:30px;letter-spacing:1px}
</style>
</head>
<body>
<div class="flyer">
  <section class="promo">
    <div class="brand-oval"><span class="brand-dot"></span><span class="brand-name">BrightPath Skills</span></div>
    <h1 class="motto"><span class="motto-line">TRAIN TODAY FOR A</span><span class="motto-line">SAFER TOMORROW</span></h1>
    <div class="photo" role="img" aria-label="Workers in hard hats and safety harnesses working at height on a crane structure against a blue sky"></div>
    <p class="contact-note">FOR A COMPLETE LIST OF WHAT WE CAN OFFER YOU, PLEASE DO NOT HESITATE IN CONTACTING OUR OFFICE ON</p>
    <div class="phone">
      <svg width="34" height="66" viewBox="0 0 34 62" aria-hidden="true"><rect x="2" y="2" width="30" height="58" rx="5" fill="#fff"/><path d="M11 20c0 10 5 18 12 22l3-4-4-3-2 2c-3-2-5-6-6-10l2-1-1-5z" fill="var(--red)"/></svg>
      <span class="phone-num">07 4510 2286</span>
    </div>
    <div class="email">
      <svg width="32" height="24" viewBox="0 0 32 24" aria-hidden="true"><rect width="32" height="24" rx="2" fill="#fff"/><path d="M3 4l13 10 13-10" fill="none" stroke="var(--red)" stroke-width="2.5"/></svg>
      <span>ADMIN@BRIGHTPATHSKILLS.COM.AU</span>
    </div>
  </section>

  <h2 class="list-title">LIST OUR COURSES AND PRICES</h2>
  <table class="price-table">
    <thead><tr><th class="col-course">Courses</th><th class="col-duration">Duration</th><th class="col-cost">Cost</th></tr></thead>
    <tbody>
      <tr><td>Safe Work at Heights</td><td class="dur">7 Day</td><td class="cost">$225</td></tr>
      <tr><td>Confined Space</td><td class="dur">7 Day</td><td class="cost">$225</td></tr>
      <tr><td>Swift Water Rescue</td><td class="dur">7 Day</td><td class="cost">$225</td></tr>
      <tr><td>Fire Extinguisher Training</td><td class="dur">7 Day</td><td class="cost">$225</td></tr>
      <tr><td>Fire Warden Training</td><td class="dur">7 Day</td><td class="cost">$225</td></tr>
      <tr><td>Breathing Apparatus Training</td><td class="dur">7 Day</td><td class="cost">$225</td></tr>
      <tr><td>Emergency Response Team Training</td><td class="dur">7 Day</td><td class="cost">$225</td></tr>
      <tr><td>Provide Emergency Care</td><td class="dur">7 Day</td><td class="cost">$225</td></tr>
      <tr><td>Road Accident Rescue</td><td class="dur">7 Day</td><td class="cost">$225</td></tr>
      <tr><td>Gas Test Atmospheres</td><td class="dur">7 Day</td><td class="cost">$225</td></tr>
      <tr><td>Confined Space Rescue</td><td class="dur">7 Day</td><td class="cost">$225</td></tr>
      <tr><td>Vertical Rescue</td><td class="dur">7 Day</td><td class="cost">$225</td></tr>
      <tr><td>Operate Breathing Apparatus</td><td class="dur">7 Day</td><td class="cost">$225</td></tr>
      <tr><td>CCBA Unit</td><td class="dur">7 Day</td><td class="cost">$225</td></tr>
      <tr><td>Render Hazardous Materials Incidents Safe</td><td class="dur">7 Day</td><td class="cost">$225</td></tr>
      <tr><td>Respond to Wildfire</td><td class="dur">7 Day</td><td class="cost">$225</td></tr>
      <tr><td>Senior First Aid Training</td><td class="dur">7 Day</td><td class="cost">$225</td></tr>
      <tr><td>Low Voltage Switchboard Rescue</td><td class="dur">7 Day</td><td class="cost">$225</td></tr>
      <tr><td>Issue Work Permits</td><td class="dur">7 Day</td><td class="cost">$225</td></tr>
      <tr><td>Fatigue Management Training (Supervisors)</td><td class="dur">7 Day</td><td class="cost">$225</td></tr>
      <tr><td>Fatigue Management Training (Workers)</td><td class="dur">7 Day</td><td class="cost">$225</td></tr>
      <tr><td>Overhead Gantry Crane Ticket</td><td class="dur">7 Day</td><td class="cost">$225</td></tr>
      <tr><td>Telehandler Ticket</td><td class="dur">7 Day</td><td class="cost">$225</td></tr>
      <tr><td>Loader Ticket</td><td class="dur">7 Day</td><td class="cost">$225</td></tr>
      <tr><td>Skidsteer Ticket</td><td class="dur">7 Day</td><td class="cost">$225</td></tr>
      <tr><td>Excavator Ticket</td><td class="dur">7 Day</td><td class="cost">$225</td></tr>
      <tr><td>High Risk Work Licence Tickets</td><td class="dur">7 Day</td><td class="cost">$225</td></tr>
      <tr><td>Standard 11</td><td class="dur">7 Day</td><td class="cost">$225</td></tr>
      <tr><td>Perform Tower Rescue</td><td class="dur">7 Day</td><td class="cost">$225</td></tr>
      <tr><td>Forklift (LF) Ticket</td><td class="dur">7 Day</td><td class="cost">$225</td></tr>
      <tr><td>EWP (WP) Ticket</td><td class="dur">7 Day</td><td class="cost">$225</td></tr>
      <tr><td>Dogging (DG) Ticket</td><td class="dur">7 Day</td><td class="cost">$225</td></tr>
      <tr><td>Non slew crane (CN) Ticket</td><td class="dur">7 Day</td><td class="cost">$225</td></tr>
      <tr><td>Vehicle Loading Crane (CV) Ticket</td><td class="dur">7 Day</td><td class="cost">$225</td></tr>
      <tr><td>Basic Scaffolding (SB) Ticket</td><td class="dur">7 Day</td><td class="cost">$225</td></tr>
      <tr><td>Intermediate scaffolding (SI) Ticket</td><td class="dur">7 Day</td><td class="cost">$225</td></tr>
      <tr><td>Advanced scaffolding (SA) Ticket</td><td class="dur">7 Day</td><td class="cost">$225</td></tr>
      <tr><td>Basic Rigging (RB) Ticket</td><td class="dur">7 Day</td><td class="cost">$225</td></tr>
      <tr><td>Health and Safety Representative Training</td><td class="dur">7 Day</td><td class="cost">$225</td></tr>
      <tr><td>Risk Management</td><td class="dur">7 Day</td><td class="cost">$225</td></tr>
    </tbody>
  </table>

  <div class="web-bar">
    <svg width="22" height="22" viewBox="0 0 22 22" aria-hidden="true"><path d="M2 2l18 7-8 2-2 8z" fill="#fff"/><path d="M12 11l7 7" stroke="#fff" stroke-width="3"/></svg>
    <span>WWW.BRIGHTPATHSKILLS.COM.AU</span>
  </div>
</div>
</body>
</html>
```